Geschäftspapiere für Patent- und Rechtsanwaltskanzei
Zielgruppe
Wir sind eine Patent- und Rechtsanwaltskanzei in Frankfurt. Unsere Zielgruppe sind sowohl die Großindustrie als auch Rechtsanwaltskanzleien.

```html
<!DOCTYPE html>
<html lang="en">
<head>
<meta charset="utf-8">
<title>Envelope Set – Hallberg-Strauss</title>
<link rel="stylesheet" href="https://fonts.googleapis.com/css2?family=Tinos:wght@400&display=swap">
<style>
  :root {
    --backdrop: #979ca5;
    --paper: #ffffff;
    --brand-orange: #e84e16;
    --brand-grey: #5a504d;
    --ink: #4a4442;
    --window-line: #b9b9b9;
  }
  * { margin: 0; padding: 0; box-sizing: border-box; }
  html, body { width: 687px; height: 1200px; overflow: hidden; }
  body {
    background: var(--backdrop);
    font-family: "Tinos", "Times New Roman", serif;
    position: relative;
  }
  .envelope {
    position: absolute;
    left: 53px;
    width: 581px;
    height: 291px;
    background: var(--paper);
    box-shadow: 0 6px 14px rgba(40, 44, 52, 0.35);
    overflow: hidden;
  }
  .envelope--front { top: 274px; }
  .envelope--back  { top: 598px; }

  .sender {
    position: absolute;
    left: 54px;
    top: 48px;
    line-height: 13.5px;
    white-space: nowrap;
  }
  .sender__tagline { font-size: 11.4px; color: var(--ink); letter-spacing: -0.2px; }
  .sender__firm { font-size: 11.4px; color: var(--brand-orange); letter-spacing: -0.2px; }

  .brand-name {
    position: absolute;
    width: 76px;
    height: 36px;
    display: flex;
    align-items: center;
    font-size: 14px;
    color: var(--brand-grey);
    letter-spacing: 0.5px;
    white-space: nowrap;
  }
  .envelope--front .brand-name { left: 290px; top: 36px; }
  .envelope--back .brand-name { left: 54px; top: 187px; }

  .address-window {
    position: absolute;
    left: 54px;
    top: 132px;
    width: 238px;
    height: 119px;
    border: 0.8px solid var(--window-line);
    border-radius: 10px;
  }

  .flap { position: absolute; left: 0; top: 0; width: 581px; height: 66px; }

  .footer-line {
    position: absolute;
    left: 54px;
    top: 233px;
    font-size: 8.1px;
    color: var(--ink);
    white-space: nowrap;
  }
  .footer-line__firm { color: var(--brand-orange); }

  .web {
    position: absolute;
    left: 410px;
    top: 233px;
    width: 105px;
    font-size: 7.9px;
    color: var(--ink);
    white-space: nowrap;
  }
  .web__bar {
    position: absolute;
    left: 410px;
    top: 250px;
    width: 105px;
    height: 11px;
    background: var(--brand-orange);
  }
</style>
</head>
<body>
  <section class="envelope envelope--front" aria-label="Envelope front">
    <div class="sender">
      <p class="sender__tagline">PATENT ATTORNEYS &amp; ATTORNEYS AT LAW</p>
      <p class="sender__firm">DR. HALLBERG-STRAUSS &amp; PARTNERS LLP</p>
    </div>
    <div class="brand-name">HALLBERG</div>
    <div class="address-window"></div>
  </section>

  <section class="envelope envelope--back" aria-label="Envelope back">
    <svg class="flap" viewBox="0 0 581 66" aria-hidden="true">
      <path d="M0 0 H581 L557 58 Q553 66 544 66 H37 Q28 66 24 58 Z" fill="var(--brand-grey)"/>
    </svg>
    <div class="brand-name">HALLBERG</div>
    <p class="footer-line">PATENT ATTORNEYS &amp; ATTORNEYS AT LAW <span class="footer-line__firm">DR. HALLBERG-STRAUSS &amp; PARTNERS LLP</span></p>
    <p class="web">WWW.HALLBERG-PATENT.COM</p>
    <div class="web__bar"></div>
  </section>
</body>
</html>
```